Web Design Project

Revamp current website adding newly designed logo and creating layout that is good on desktops, tablets, and cell phones.

Current website can be viewed at www.venkirainteriors.com

Will you see the website is small but graphics heavy in the gallery. The gallery needs to be setup so that it is easy to maintain the links and update the photos.

Needs to have high visual impact.

I need a new logo and website layout designed for my partner's business. This is a birthday present. His business is interior painting, wallpapering and design. He also has access to a wide variety of products including carpet, fabrics, furniture, wallpaper, tile, countertops, etc. I have attached some screen shots of his website for reference. He is a one man shop and has a stellar reputation with his customers. He is on-time, very tidy, excellent with animals, and always finishes on time and on budget. There are no restrictions on colors or fonts. The logo needs to work well with the website, business cards and printed materials. The website needs to flow content for device size so it looks just as good on a cell phone or tablet as it does on a desktop computer. Whatever the heck that's called! Thanks. I am looking forward to seeing everyone's ideas.

Target Market(s)

Consumers looking for interior design, painting, and wallpapering as well as interior products such as flooring, window treatments, reupholstering, counter tops, etc.

Industry/Entity Type

Cell Phone

Requirements
Must have
• Clean, sharp, visual impact (at least on the home page)
Should not have
• Clutter.

```html
<!DOCTYPE html>
<html lang="en">
<head>
<meta charset="utf-8">
<title>Venkira Interior Designs — Home</title>
<link href="https://fonts.googleapis.com/css2?family=EB+Garamond:wght@400;600&family=Arvo&display=swap" rel="stylesheet">
<style>
  :root {
    --page: #ffffff;
    --ink: #1a1a1a;
    --navy: #17153a;
    --muted-heading: #a9a9a9;
    --nav-active: #6a9a3a;
    --rule: #c9c9c9;
    --teal: #236878;
    --green-bar: #6aa23a;
    --icon: #111111;
    --photo-warm: #cdb58d;
    --photo-dark: #4a3020;
  }
  * { box-sizing: border-box; margin: 0; padding: 0; }
  html, body { width: 1200px; height: 1000px; overflow: hidden; background: var(--page); }
  body { position: relative; font-family: Arial, Helvetica, sans-serif; color: var(--ink); }

  .site-header {
    position: absolute; left: 70px; top: 0; width: 1040px; height: 179px;
    border-top: 3px solid #dcdcdc;
    border-bottom: 2px solid var(--rule);
    box-shadow: 0 2px 3px rgba(0,0,0,.12);
  }
  .brand {
    position: absolute; left: 372px; top: 38px; width: 310px;
    display: flex; align-items: center; gap: 12px;
    font-family: "EB Garamond", serif; font-weight: 600; color: var(--navy);
  }
  .brand-square { width: 58px; height: 58px; background: var(--navy); flex: none; }
  .brand-name { line-height: 1; }
  .brand-name .line1 { display: block; font-size: 44px; letter-spacing: 1px; }
  .brand-name .line2 { display: block; font-size: 22px; letter-spacing: 1px; margin-top: 2px; }

  .main-nav {
    position: absolute; left: 325px; top: 142px; width: 397px;
    border-top: 1px solid var(--rule); height: 30px;
  }
  .main-nav a {
    position: absolute; top: 12px; font-size: 9.5px; color: var(--ink); text-decoration: none;
  }
  .main-nav a.active { color: var(--nav-active); }

  .hero-photo { position: absolute; left: 405px; top: 209px; width: 375px; height: 209px;
    background: linear-gradient(90deg, var(--photo-dark) 0%, var(--photo-warm) 30%, #d8c6a0 60%, var(--photo-dark) 100%); }

  .tagline {
    position: absolute; left: 340px; top: 432px; width: 505px; text-align: center;
    font-family: "EB Garamond", serif; font-size: 21px; color: var(--muted-heading);
  }
  .intro {
    position: absolute; left: 420px; top: 467px; width: 345px; text-align: center;
    font-size: 10.5px; line-height: 20px;
  }
  .motto {
    position: absolute; left: 400px; top: 570px; width: 385px; text-align: center;
    font-family: "Arvo", serif; font-size: 13.5px; line-height: 22px; color: #333;
  }

  .site-footer {
    position: absolute; left: 239px; top: 664px; width: 707px; height: 33px; background: var(--teal);
    color: #fff; font-size: 8px;
  }
  .site-footer .copyright { position: absolute; left: 10px; top: 12px; }
  .social { position: absolute; right: 8px; top: 9px; display: flex; gap: 5px; }
  .social span { width: 17px; height: 17px; background: var(--icon); border: 1px solid #ddd; }

  .gallery-screen {
    position: absolute; left: 88px; top: 684px; width: 308px; height: 246px;
    background: #fff; transform: rotate(-6deg);
    box-shadow: 8px 14px 22px rgba(0,0,0,.35), 0 0 2px rgba(0,0,0,.2);
    font-size: 4px;
  }
  .gallery-screen .mini-brand {
    position: absolute; left: 104px; top: 20px; display: flex; align-items: center; gap: 4px;
    font-family: "EB Garamond", serif; font-weight: 600; color: var(--navy); line-height: 1;
  }
  .mini-brand .brand-square { width: 16px; height: 16px; }
  .mini-brand .line1 { display: block; font-size: 12px; }
  .mini-brand .line2 { display: block; font-size: 6px; }
  .mini-nav { position: absolute; left: 0; top: 44px; width: 100%; border-bottom: 1px solid var(--rule); height: 22px; }
  .mini-nav ul { position: absolute; left: 92px; top: 9px; width: 130px; display: flex; justify-content: space-between; list-style: none; border-top: 1px solid #ddd; padding-top: 3px; }
  .mini-nav li.active { color: var(--nav-active); }
  .mini-title { position: absolute; top: 72px; width: 100%; text-align: center; color: #999; font-size: 5px; }
  .thumb-grid {
    position: absolute; left: 52px; top: 82px; width: 230px;
    display: grid; grid-template-columns: repeat(6, 32px); gap: 7px 6px;
  }
  .thumb-grid span { height: 31px; background: linear-gradient(135deg, #8a6a48, #d9cdb4); }
  .thumb-grid span:nth-child(3n) { background: linear-gradient(135deg, #cfcac0, #7d7568); }
  .thumb-grid span:nth-child(4n+1) { background: linear-gradient(135deg, #5a3a2a, #b08a60); }
  .mini-more { position: absolute; top: 228px; width: 100%; text-align: center; color: var(--nav-active); }
  .mini-footer { position: absolute; left: 40px; top: 235px; width: 230px; height: 9px; background: var(--green-bar); color: #fff; padding: 2px 4px; font-size: 3.5px; }
</style>
</head>
<body>
  <header class="site-header">
    <div class="brand">
      <span class="brand-square"></span>
      <span class="brand-name"><span class="line1">VENKIRA</span><span class="line2">INTERIOR DESIGNS</span></span>
    </div>
    <nav class="main-nav">
      <a class="active" href="#" style="left:1px">home</a>
      <a href="#" style="left:87px">about</a>
      <a href="#" style="left:172px">products</a>
      <a href="#" style="left:272px">gallery</a>
      <a href="#" style="left:362px">contact</a>
    </nav>
  </header>

  <main>
    <div class="hero-photo" role="img" aria-label="Photo of a traditional hallway with dark wood door frames, striped wallpaper, framed prints and a pendant light"></div>
    <h1 class="tagline">A wonderful new look is within anyone's reach!</h1>
    <p class="intro">With over 30 years of experience, Venkira Interior Designs provides workmanship for the domestic and commercial markets. Whether you are starting with a small project or a large project, we are ready to bring your ideas to life. It doesn't take a big budget to achieve dramatic effects.</p>
    <p class="motto">Your home is a reflection of your personality. Let it tell people how wonderful you are.</p>
  </main>

  <footer class="site-footer">
    <span class="copyright">© 2014 Venkira</span>
    <div class="social" aria-label="Social links"><span></span><span></span><span></span></div>
  </footer>

  <section class="gallery-screen" aria-label="Gallery page layout">
    <div class="mini-brand">
      <span class="brand-square"></span>
      <span><span class="line1">VENKIRA</span><span class="line2">INTERIOR DESIGNS</span></span>
    </div>
    <nav class="mini-nav"><ul><li>home</li><li>about</li><li>products</li><li class="active">gallery</li><li>contact</li></ul></nav>
    <div class="mini-title">gallery</div>
    <div class="thumb-grid" role="img" aria-label="Grid of room photographs showing finished interiors">
      <span></span><span></span><span></span><span></span><span></span><span></span>
      <span></span><span></span><span></span><span></span><span></span><span></span>
      <span></span><span></span><span></span><span></span><span></span><span></span>
      <span></span><span></span><span></span><span></span><span></span><span></span>
    </div>
    <div class="mini-more">click here</div>
    <div class="mini-footer">© 2014 Venkira Interior Designs. All rights reserved.</div>
  </section>
</body>
</html>
```